Bellmoor Commercial Finance Information Brochure

This brochure will be sent out to clients via A4 PDF on an email to showcase what our company has to offer. We are a commercial finance brokerage, that specialises in property finance. We would like to see designs following our colour scheme. The final design should demonstrate our professionalism and reliability.
I have attached our logo and also a few bullet points on our information and what we can offer. These can be slightly reworded for conciseness. Or leave the text sections as filler and I can fill these in.
I have also attached an overview of our colour scheme and design styling for your consideration.
Target Market(s)
Property Developers
Industry/Entity Type
Financial Services

```html
<!DOCTYPE html>
<html lang="en">
<head>
<meta charset="utf-8">
<title>Bellmoor Commercial Finance Brochure</title>
<link href="https://fonts.googleapis.com/css2?family=Montserrat:wght@500;600;700&family=Open+Sans:wght@400;600&display=swap" rel="stylesheet">
<style>
  :root {
    --blue: #2540a3;
    --blue-deep: #1d3591;
    --green: #2f8f3c;
    --green-bright: #3f9e3a;
    --ink: #4a4f5a;
    --paper: #ffffff;
    --backdrop: #e9e9ea;
    --heading: 'Montserrat', Arial, sans-serif;
    --body: 'Open Sans', Arial, sans-serif;
  }
  * { box-sizing: border-box; margin: 0; padding: 0; }
  html, body { width: 720px; height: 1200px; overflow: hidden; }
  body { background: var(--backdrop); position: relative; font-family: var(--body); color: var(--ink); }

  .page { position: absolute; background: var(--paper); overflow: hidden; box-shadow: 0 2px 8px rgba(0,0,0,.12); }
  .page-stripes { position: absolute; left: 0; bottom: 0; width: 100%; height: 22px; }

  /* Front cover */
  .front-cover { left: 370px; top: 100px; width: 330px; height: 467px; }
  .brand-name { position: absolute; display: flex; align-items: center; gap: 6px; font-family: var(--heading); font-weight: 700; white-space: nowrap; }
  .brand-name .brand-square { width: 10px; height: 10px; background: var(--green); }
  .front-cover .brand-name { left: 22px; top: 30px; font-size: 16px; color: var(--blue); letter-spacing: .5px; }
  .cover-photo { position: absolute; left: 70px; top: 14px; width: 260px; height: 300px;
    background: linear-gradient(180deg, #9ec3e0 0%, #c9dced 40%, #c7b79a 72%, #a58f6c 100%);
    border-top-left-radius: 160px 60px; }
  .cover-banner { position: absolute; left: 86px; top: 262px; width: 210px; height: 56px; }
  .cover-banner::before { content: ""; position: absolute; left: 8px; top: 7px; width: 100%; height: 100%; background: var(--green); }
  .cover-banner-text { position: absolute; inset: 0; background: var(--blue); color: #fff; font-family: var(--heading); font-weight: 700; font-size: 13.5px; line-height: 1.3; padding: 10px 14px; }
  .cover-web { position: absolute; right: 26px; top: 398px; font-family: var(--heading); font-weight: 500; font-size: 10.5px; color: var(--blue); letter-spacing: .4px; }

  /* Back cover */
  .back-cover { left: 20px; top: 100px; width: 330px; height: 467px;
    background: linear-gradient(170deg, #3f9a3c 0%, #1f7a62 35%, #1d5f86 65%, #233f9e 100%); color: #fff; text-align: center; }
  .back-photo { position: absolute; inset: 0 0 auto 0; height: 200px; opacity: .25;
    background: linear-gradient(180deg, #0e4a30 0%, rgba(14,74,48,0) 100%); }
  .back-cover .brand-name { left: 50%; top: 190px; transform: translateX(-50%); font-size: 22px; color: #fff; letter-spacing: 1px; }
  .back-cover .brand-name .brand-square { background: #fff; width: 12px; height: 12px; }
  .back-contact { position: absolute; left: 0; right: 0; top: 240px; line-height: 1.6; }
  .back-phone { font-family: var(--heading); font-weight: 700; font-size: 18px; }
  .back-line { font-size: 10.5px; }
  .back-address { font-size: 9.5px; margin-top: 12px; line-height: 1.5; }
  .back-strip { position: absolute; left: 0; right: 0; bottom: 0; height: 8px; background: var(--green-bright); }

  /* Inner spread */
  .spread-left { left: 20px; top: 597px; width: 340px; height: 481px; }
  .spread-right { left: 360px; top: 597px; width: 340px; height: 481px; }
  .spine { position: absolute; left: 359px; top: 597px; width: 2px; height: 481px; background: linear-gradient(90deg, rgba(0,0,0,.12), rgba(0,0,0,0)); }

  .finance-photo { position: absolute; left: 0; top: 0; width: 340px; height: 180px;
    background: linear-gradient(160deg, #1e5d8e 0%, #5fa1c4 45%, #d9e6ef 100%); }
  .welcome-panel { position: absolute; left: 22px; top: 110px; width: 170px; height: 150px; padding: 14px 14px;
    background: linear-gradient(135deg, var(--green) 0%, #1f6f78 55%, var(--blue) 100%); color: #fff; }
  .welcome-kicker { font-family: var(--heading); font-size: 9px; font-weight: 500; }
  .welcome-title { font-family: var(--heading); font-size: 13px; font-weight: 600; line-height: 1.25; margin: 2px 0 7px; }
  .welcome-text { font-size: 6.6px; line-height: 1.45; }

  .apart { position: absolute; left: 204px; top: 186px; width: 122px; }
  .apart-heading { font-family: var(--heading); font-weight: 700; font-size: 9.5px; line-height: 1.3; color: var(--blue); }
  .apart-heading em { font-style: normal; color: var(--green); }
  .body-copy { font-size: 6.4px; line-height: 1.5; color: var(--ink); }
  .apart .body-copy { margin-top: 5px; }
  .founded { position: absolute; left: 22px; top: 282px; width: 300px; }

  .why-heading { position: absolute; left: 0; right: 0; top: 326px; text-align: center; font-family: var(--heading); font-weight: 700; font-size: 12px; color: var(--blue); }
  .why-heading em { font-style: normal; color: var(--green); }
  .reasons { position: absolute; left: 18px; right: 18px; top: 350px; display: flex; gap: 10px; }
  .reason-card { flex: 1; border: 1px solid #dfe3e8; padding: 10px 8px; text-align: center; height: 88px; background: #fff; }
  .reason-icon { width: 16px; height: 16px; display: block; margin: 0 auto 3px; }
  .reason-title { font-family: var(--heading); font-size: 9px; font-weight: 600; color: var(--green); margin-bottom: 4px; }

  .hands-photo { position: absolute; left: 0; top: 0; width: 340px; height: 168px;
    background: linear-gradient(120deg, #efe7dc 0%, #f7f3ee 45%, #d9c3a6 100%); }
  .text-col { position: absolute; top: 184px; }
  .col-one { left: 20px; width: 140px; }
  .col-two { left: 172px; width: 150px; }
  .text-col .body-copy + .body-copy { margin-top: 7px; }
  .house-photo { position: absolute; left: 186px; top: 330px; width: 150px; height: 112px;
    background: linear-gradient(180deg, #ffffff 0%, #eef0f2 50%, #c6b4a2 100%); }
</style>
</head>
<body>

  <!-- Back cover -->
  <section class="page back-cover">
    <div class="back-photo" role="img" aria-label="Faint photo of hands passing a small model house across a desk"></div>
    <div class="brand-name"><span class="brand-square"></span>Bellmoor Finance</div>
    <div class="back-contact">
      <p class="back-phone">0800 000 4127</p>
      <p class="back-line">enquiries@bellmoorfinance.co.uk</p>
      <p class="back-line">www.bellmoorfinance.co.uk</p>
      <p class="back-address">Unit 7, Harlow Mill Park, Ferndale Road,<br>Lancaster, LA2 9XT</p>
    </div>
    <div class="back-strip"></div>
  </section>

  <!-- Front cover -->
  <section class="page front-cover">
    <div class="cover-photo" role="img" aria-label="Photo of construction workers in hi-vis vests walking onto a building site"></div>
    <div class="brand-name"><span class="brand-square"></span>Bellmoor Finance</div>
    <div class="cover-banner">
      <div class="cover-banner-text">Contact BELLMOOR<br>Commercial FINANCE</div>
    </div>
    <p class="cover-web">www.bellmoorfinance.co.uk</p>
    <svg class="page-stripes" viewBox="0 0 330 22" preserveAspectRatio="none">
      <polygon points="0,14 150,10 150,22 0,22" fill="#3f9e3a"/>
      <polygon points="156,10 330,2 330,10 166,13" fill="#2540a3"/>
      <polygon points="146,16 330,8 330,22 140,22" fill="#3f9e3a"/>
    </svg>
  </section>

  <!-- Inner spread, left page -->
  <section class="page spread-left">
    <div class="finance-photo" role="img" aria-label="Photo of a businessman with finance chart overlays and a small model house"></div>
    <div class="welcome-panel">
      <p class="welcome-kicker">Welcome to</p>
      <h2 class="welcome-title">Bellmoor<br>Commercial Finance</h2>
      <p class="welcome-text">At Bellmoor Finance, we're not your typical finance firm. Our story began with a simple idea: to create a seamless process that empowers developers to effortlessly arrange financing for their building projects.</p>
    </div>
    <div class="apart">
      <h3 class="apart-heading">What sets us apart? <em>Well, we've walked in your shoes.</em></h3>
      <p class="body-copy">As former lenders and developers, we know the delays that slow deals down and the hours lost gathering paperwork.</p>
    </div>
    <p class="body-copy founded">That's why we founded Bellmoor Finance: to be the clear and reliable link between developers and lenders. With our expertise, we guide you through every step, from first call to final funding.</p>
    <h3 class="why-heading">Why choose <em>Bellmoor Commercial Finance?</em></h3>
    <div class="reasons">
      <article class="reason-card">
        <svg class="reason-icon" viewBox="0 0 16 16"><circle cx="8" cy="8" r="6" fill="none" stroke="#2f8f3c" stroke-width="1.4"/><path d="M8 4.5V8l2.5 1.5" fill="none" stroke="#2f8f3c" stroke-width="1.4"/></svg>
        <h4 class="reason-title">Efficiency</h4>
        <p class="body-copy">Our aim is to cut the hours spent arranging deals, so we do the hard work for you.</p>
      </article>
      <article class="reason-card">
        <svg class="reason-icon" viewBox="0 0 16 16"><path d="M8 2l1.8 3.8 4.2.5-3.1 2.9.8 4.1L8 11.3 4.3 13.3l.8-4.1L2 6.3l4.2-.5z" fill="none" stroke="#2f8f3c" stroke-width="1.2"/></svg>
        <h4 class="reason-title">Experience</h4>
        <p class="body-copy">Having worked on both sides of finance, we can offer options few other brokers can.</p>
      </article>
      <article class="reason-card">
        <svg class="reason-icon" viewBox="0 0 16 16"><path d="M3 8.5l3 3 7-7" fill="none" stroke="#2f8f3c" stroke-width="1.6"/></svg>
        <h4 class="reason-title">Reliability</h4>
        <p class="body-copy">Strong ties with lenders and developers mean we deliver on what we promise.</p>
      </article>
    </div>
    <svg class="page-stripes" viewBox="0 0 340 22" preserveAspectRatio="none">
      <polygon points="0,14 340,8 340,14 0,22" fill="#3f9e3a"/>
      <polygon points="200,10 340,4 340,8 210,11" fill="#2540a3"/>
    </svg>
  </section>

  <!-- Inner spread, right page -->
  <section class="page spread-right">
    <div class="hands-photo" role="img" aria-label="Photo of hands holding a jar of coins with a sprouting plant beside a model house"></div>
    <div class="text-col col-one">
      <p class="body-copy">As former lenders and developers, we understand the gaps in today's market and the stress of chasing information. Our process links developers and lenders with clear, swift communication and no wasted time.</p>
      <p class="body-copy">With our background in asset management, we can call on a wide book of lenders for non-traditional funding.</p>
    </div>
    <div class="text-col col-two">
      <p class="body-copy">Bellmoor Finance was created to meet a need for efficiency. We use modern tools to secure the best options quickly, and we take care of the paperwork so you can focus on building.</p>
      <p class="body-copy">We know the questions lenders ask, so we gather what is needed from day one and keep the process calm for you.</p>
    </div>
    <div class="house-photo" role="img" aria-label="Photo of a hand holding a small white model house"></div>
    <svg class="page-stripes" viewBox="0 0 340 22" preserveAspectRatio="none">
      <polygon points="0,14 340,6 340,12 0,22" fill="#3f9e3a"/>
      <polygon points="120,11 340,2 340,6 130,12" fill="#2540a3"/>
    </svg>
  </section>
  <div class="spine"></div>

</body>
</html>
```